Pet store web design

I would like to redesign my current online store (http://brindlecove.example)
I'm looking for a clean, modern design. Any ideas are welcome..

Industry/Entity Type

Pet

Number of Pages Required

3 page

```html
<!DOCTYPE html>
<html lang="en">
<head>
<meta charset="utf-8">
<title>Brindle Cove – Pet Store</title>
<link href="https://fonts.googleapis.com/css2?family=Open+Sans:wght@400;600;700&display=swap" rel="stylesheet">
<style>
:root{
  --yellow:#ffcc1a;
  --yellow-soft:#fff4c4;
  --footer-bg:#fff8dc;
  --grey-bg:#efefef;
  --panel:#ffffff;
  --text:#555555;
  --muted:#999999;
  --line:#dddddd;
  --dark:#333333;
}
*{box-sizing:border-box;margin:0;padding:0}
html,body{width:778px;height:1200px;overflow:hidden}
body{font-family:"Open Sans",Arial,sans-serif;color:var(--text);background:#fff;font-size:8px;position:relative}
.site-header{height:85px;position:relative;background:#fff}
.brand{position:absolute;left:72px;top:18px;display:flex;align-items:center;gap:6px;background:var(--yellow);border-radius:18px;padding:8px 14px}
.brand-name{font-weight:700;font-size:14px;color:var(--dark)}
.brand-dot{width:12px;height:12px;border-radius:50%;background:#fff}
.search{position:absolute;left:450px;top:14px;width:82px;height:14px;border-radius:7px;background:var(--yellow-soft);border:1px solid var(--yellow);font-size:6px;color:var(--muted);padding:2px 8px}
.cart{position:absolute;left:560px;top:13px;display:flex;align-items:center;gap:5px}
.cart-btn{background:var(--yellow);border-radius:7px;font-size:6px;padding:3px 7px;color:var(--dark)}
.social{position:absolute;left:640px;top:12px;display:flex;gap:7px}
.social span{width:12px;height:12px;border-radius:50%;background:var(--yellow)}
.top-nav{position:absolute;right:72px;top:46px;display:flex;gap:20px;font-size:7px;font-weight:600;color:var(--text)}
.main{background:var(--grey-bg);height:873px;position:relative}
.sidebar{position:absolute;left:72px;top:14px;width:140px;height:276px;background:var(--panel)}
.sidebar h3{background:var(--yellow);font-size:8px;text-align:center;padding:6px 0;font-weight:600;color:var(--dark)}
.cat-list{list-style:none;padding:8px 10px;font-size:6.5px;line-height:11px}
.cat-list li{display:flex;justify-content:space-between}
.cat-list .sub{padding-left:10px}
.cat-list .active{background:var(--yellow-soft);color:var(--dark)}
.cat-list .toggle{width:9px;height:9px;border-radius:50%;border:1px solid var(--line)}
.catalog{position:absolute;left:228px;top:14px;width:477px;height:850px;background:var(--panel);padding:10px 14px}
.toolbar{display:flex;align-items:center;gap:10px;font-size:6px;color:var(--muted);height:14px}
.toolbar .box{width:8px;height:8px;background:var(--muted)}
.toolbar .pill{background:var(--yellow-soft);border:1px solid var(--yellow);border-radius:3px;padding:1px 8px}
.grid{display:grid;grid-template-columns:repeat(3,1fr);gap:34px 24px;margin-top:12px}
.card{height:157px}
.card-photo{height:100px;border:1px solid var(--line);background:linear-gradient(160deg,#fdfdfd,#f1e9e9)}
.card-photo.dark{background:linear-gradient(160deg,#fdfdfd,#e8e2d6)}
.card-photo.gold{background:linear-gradient(160deg,#fdfdfd,#f4ecc8)}
.card-name{font-size:6.5px;margin-top:8px;color:var(--text)}
.card-price{font-size:6.5px;margin-top:4px;color:var(--dark);font-weight:600}
.card-actions{display:flex;align-items:center;gap:6px;margin-top:6px}
.card-actions svg{width:10px;height:10px}
.add-btn{margin-left:auto;background:var(--yellow);border-radius:8px;font-size:6px;font-weight:600;padding:3px 9px;color:var(--dark)}
.pager{position:absolute;left:14px;right:14px;bottom:14px;display:flex;justify-content:space-between;font-size:6.5px;align-items:center}
.pager span{display:flex;align-items:center;gap:4px}
.pager i{width:12px;height:12px;border-radius:50%;border:1px solid var(--muted);display:inline-block}
.newsletter{height:65px;display:flex;align-items:center;justify-content:space-between;padding:0 72px;font-size:7px;font-weight:600}
.newsletter b{color:var(--yellow)}
.newsletter .field{width:190px;height:18px;border:1px solid var(--muted);border-radius:9px;font-size:6px;color:var(--muted);padding:4px 10px;font-weight:400}
.site-footer{background:var(--footer-bg);height:155px;padding:16px 72px;display:flex;gap:30px}
.site-footer h4{font-size:7px;color:var(--dark);margin-bottom:8px}
.col ul{list-style:none;font-size:6.5px;line-height:11px}
.col.wide{margin-left:auto;width:160px;font-size:6px;line-height:9px}
.pay{display:flex;gap:8px;margin-top:6px;align-items:center;font-size:9px;font-weight:700;color:var(--dark)}
.legal{position:absolute;left:0;bottom:0;width:778px;height:22px;background:var(--yellow);font-size:6px;text-align:center;line-height:22px;color:var(--dark)}
</style>
</head>
<body>
<header class="site-header">
  <div class="brand"><span class="brand-dot"></span><span class="brand-name">Brindle Cove</span></div>
  <div class="search">Search</div>
  <div class="cart">
    <svg width="12" height="10" viewBox="0 0 12 10"><path d="M0 1h2l2 6h6l1-4H3" fill="none" stroke="#ffcc1a" stroke-width="1.4"/><circle cx="5" cy="9" r="1" fill="#ffcc1a"/><circle cx="9" cy="9" r="1" fill="#ffcc1a"/></svg>
    <span class="cart-btn">Cart (0)</span>
  </div>
  <div class="social"><span></span><span></span><span></span></div>
  <nav class="top-nav"><span>MY ACCOUNT</span><span>MY CART</span><span>CHECKOUT</span><span>MY WISHLIST</span><span>LOGIN/REGISTER</span></nav>
</header>

<main class="main">
  <aside class="sidebar">
    <h3>CATEGORIES</h3>
    <ul class="cat-list">
      <li>DOG <i class="toggle"></i></li>
      <li class="sub">Dog Hats</li>
      <li class="sub active">Pet Clothes</li>
      <li class="sub">Pet Bowls</li>
      <li class="sub">Pet Gate Extensions</li>
      <li class="sub">Dog Collars</li>
      <li class="sub">Pet Gates</li>
      <li class="sub">Pet Waste Disposal</li>
      <li class="sub">Dog Treadmills</li>
      <li>&nbsp;</li>
      <li>CAT <i class="toggle"></i></li>
      <li>FISH <i class="toggle"></i></li>
      <li>BIRD <i class="toggle"></i></li>
      <li>SMALL PET <i class="toggle"></i></li>
    </ul>
  </aside>

  <section class="catalog">
    <div class="toolbar">
      <span class="box"></span><span class="box"></span>
      <span>Page 1 2 3 4 5</span>
      <span>Items 1 to 12 of 97 total</span>
      <span>Show <span class="pill">12</span></span>
      <span>Sort by <span class="pill">Position</span></span>
    </div>
    <div class="grid">
      <article class="card"><div class="card-photo" role="img" aria-label="Product photo of a dog in a horse costume"></div><p class="card-name">Cute Horse Dog Costume</p><p class="card-price">$28.97</p><div class="card-actions"><svg viewBox="0 0 10 10"><path d="M5 9L1.5 5.5A2 2 0 015 2.5a2 2 0 013.5 3z" fill="none" stroke="#999"/></svg><svg viewBox="0 0 10 10"><rect x="1" y="2" width="8" height="6" fill="none" stroke="#999"/></svg><span class="add-btn">ADD TO CART</span></div></article>
      <article class="card"><div class="card-photo dark" role="img" aria-label="Product photo of a dog in a pirate costume"></div><p class="card-name">Pirate Outfit Dog Costume</p><p class="card-price">$28.97</p><div class="card-actions"><svg viewBox="0 0 10 10"><path d="M5 9L1.5 5.5A2 2 0 015 2.5a2 2 0 013.5 3z" fill="none" stroke="#999"/></svg><svg viewBox="0 0 10 10"><rect x="1" y="2" width="8" height="6" fill="none" stroke="#999"/></svg><span class="add-btn">ADD TO CART</span></div></article>
      <article class="card"><div class="card-photo gold" role="img" aria-label="Product photo of a dog in a bee costume"></div><p class="card-name">Honey Bee Dog Costume</p><p class="card-price">$28.97</p><div class="card-actions"><svg viewBox="0 0 10 10"><path d="M5 9L1.5 5.5A2 2 0 015 2.5a2 2 0 013.5 3z" fill="none" stroke="#999"/></svg><svg viewBox="0 0 10 10"><rect x="1" y="2" width="8" height="6" fill="none" stroke="#999"/></svg><span class="add-btn">ADD TO CART</span></div></article>

      <article class="card"><div class="card-photo" role="img" aria-label="Product photo of a dog in a horse costume"></div><p class="card-name">Cute Horse Dog Costume</p><p class="card-price">$28.97</p><div class="card-actions"><svg viewBox="0 0 10 10"><path d="M5 9L1.5 5.5A2 2 0 015 2.5a2 2 0 013.5 3z" fill="none" stroke="#999"/></svg><svg viewBox="0 0 10 10"><rect x="1" y="2" width="8" height="6" fill="none" stroke="#999"/></svg><span class="add-btn">ADD TO CART</span></div></article>
      <article class="card"><div class="card-photo dark" role="img" aria-label="Product photo of a dog in a pirate costume"></div><p class="card-name">Pirate Outfit Dog Costume</p><p class="card-price">$28.97</p><div class="card-actions"><svg viewBox="0 0 10 10"><path d="M5 9L1.5 5.5A2 2 0 015 2.5a2 2 0 013.5 3z" fill="none" stroke="#999"/></svg><svg viewBox="0 0 10 10"><rect x="1" y="2" width="8" height="6" fill="none" stroke="#999"/></svg><span class="add-btn">ADD TO CART</span></div></article>
      <article class="card"><div class="card-photo gold" role="img" aria-label="Product photo of a dog in a bee costume"></div><p class="card-name">Honey Bee Dog Costume</p><p class="card-price">$28.97</p><div class="card-actions"><svg viewBox="0 0 10 10"><path d="M5 9L1.5 5.5A2 2 0 015 2.5a2 2 0 013.5 3z" fill="none" stroke="#999"/></svg><svg viewBox="0 0 10 10"><rect x="1" y="2" width="8" height="6" fill="none" stroke="#999"/></svg><span class="add-btn">ADD TO CART</span></div></article>

      <article class="card"><div class="card-photo" role="img" aria-label="Product photo of a dog in a horse costume"></div><p class="card-name">Cute Horse Dog Costume</p><p class="card-price">$28.97</p><div class="card-actions"><svg viewBox="0 0 10 10"><path d="M5 9L1.5 5.5A2 2 0 015 2.5a2 2 0 013.5 3z" fill="none" stroke="#999"/></svg><svg viewBox="0 0 10 10"><rect x="1" y="2" width="8" height="6" fill="none" stroke="#999"/></svg><span class="add-btn">ADD TO CART</span></div></article>
      <article class="card"><div class="card-photo dark" role="img" aria-label="Product photo of a dog in a pirate costume"></div><p class="card-name">Pirate Outfit Dog Costume</p><p class="card-price">$28.97</p><div class="card-actions"><svg viewBox="0 0 10 10"><path d="M5 9L1.5 5.5A2 2 0 015 2.5a2 2 0 013.5 3z" fill="none" stroke="#999"/></svg><svg viewBox="0 0 10 10"><rect x="1" y="2" width="8" height="6" fill="none" stroke="#999"/></svg><span class="add-btn">ADD TO CART</span></div></article>
      <article class="card"><div class="card-photo gold" role="img" aria-label="Product photo of a dog in a bee costume"></div><p class="card-name">Honey Bee Dog Costume</p><p class="card-price">$28.97</p><div class="card-actions"><svg viewBox="0 0 10 10"><path d="M5 9L1.5 5.5A2 2 0 015 2.5a2 2 0 013.5 3z" fill="none" stroke="#999"/></svg><svg viewBox="0 0 10 10"><rect x="1" y="2" width="8" height="6" fill="none" stroke="#999"/></svg><span class="add-btn">ADD TO CART</span></div></article>

      <article class="card"><div class="card-photo" role="img" aria-label="Product photo of a dog in a horse costume"></div><p class="card-name">Cute Horse Dog Costume</p><p class="card-price">$28.97</p><div class="card-actions"><svg viewBox="0 0 10 10"><path d="M5 9L1.5 5.5A2 2 0 015 2.5a2 2 0 013.5 3z" fill="none" stroke="#999"/></svg><svg viewBox="0 0 10 10"><rect x="1" y="2" width="8" height="6" fill="none" stroke="#999"/></svg><span class="add-btn">ADD TO CART</span></div></article>
      <article class="card"><div class="card-photo dark" role="img" aria-label="Product photo of a dog in a pirate costume"></div><p class="card-name">Pirate Outfit Dog Costume</p><p class="card-price">$28.97</p><div class="card-actions"><svg viewBox="0 0 10 10"><path d="M5 9L1.5 5.5A2 2 0 015 2.5a2 2 0 013.5 3z" fill="none" stroke="#999"/></svg><svg viewBox="0 0 10 10"><rect x="1" y="2" width="8" height="6" fill="none" stroke="#999"/></svg><span class="add-btn">ADD TO CART</span></div></article>
      <article class="card"><div class="card-photo gold" role="img" aria-label="Product photo of a dog in a bee costume"></div><p class="card-name">Honey Bee Dog Costume</p><p class="card-price">$28.97</p><div class="card-actions"><svg viewBox="0 0 10 10"><path d="M5 9L1.5 5.5A2 2 0 015 2.5a2 2 0 013.5 3z" fill="none" stroke="#999"/></svg><svg viewBox="0 0 10 10"><rect x="1" y="2" width="8" height="6" fill="none" stroke="#999"/></svg><span class="add-btn">ADD TO CART</span></div></article>
    </div>
    <div class="pager"><span><i></i>Previous Page</span><span>Next Page<i></i></span></div>
  </section>
</main>

<section class="newsletter">
  <p>KEEP UP TO DATE ON THE LATEST FROM BRINDLE COVE! <b>SIGN UP HERE</b></p>
  <div class="field">Enter email address</div>
</section>

<footer class="site-footer">
  <div class="col"><h4>SERVICES</h4><ul><li>Pet Grooming</li><li>Pet Adoption</li><li>DIY Dog Wash</li><li>Pet Guide</li><li>Puppy School</li></ul></div>
  <div class="col"><h4>SHOPPING ONLINE</h4><ul><li>Delivery Information</li><li>Privacy Policy</li><li>Returns Policy</li><li>Terms and Conditions</li><li>FAQs</li></ul></div>
  <div class="col"><h4>&nbsp;</h4><ul><li>About Us</li><li>Careers</li><li>Pet Blog</li><li>Site Map</li><li>Contact Us</li></ul></div>
  <div class="col wide"><h4>GIVING PET NEEDS</h4><p>We care about every pet and give a share of each order to local shelters and rescue groups in our area.</p><h4 style="margin-top:10px">WE ACCEPT</h4><div class="pay"><span>Kestrelcard</span><span>Pennyrail</span><span>Loopmark</span></div></div>
</footer>
<div class="legal">© 2024 brindlecove.example · All rights reserved</div>
</body>
</html>
```